Zestra Design Prize - $10,000 tablet app design contest, Magazine Category

Zestra is a marketplace for uSlate App Templates (similar to PageLoom templates). We want you to design an app template for sale in our marketplace which targets B2B or B2C Magazine Apps (uSlate Apps created for examples such as Alumni magazine, employee magazine, sports magazine, fashion magazine etc).

It’s up to you to create pages or features for the App Template that you think are appropriate. Creativity will be rewarded! Here are some example pages or features that you could create:

• Contents
• Editor’s letter
• Event calendar
• News page
• Feature article
• Business articles
• Social media integration
• Animations and video

Your design should be Vibrant, Engaging and Contemporary. If you have an uSlate, download Zestra Viewer and download template examples in the download tab.

Your entry must include:
• A brief description of your template
• Preview images of all pages of your template

Attached to this project are free templates to help you get started with your design. We have included:
1. A free portfolio template for designers/photographers
2. Icons and artwork to use in your template
3. Blank pages template
4. Form template
5. Video ad template

If you are selected as a finalist you will be required to submit an .oproject file containing:
• Your LayoutCraft source files
• Preview images of your template
• All creative / stock assets used in the template (animations, video etc.)
• A text file with instructions on how to update the template
• A metadata .txt file containing template details and your information

How to enter:
1. Register at Marketplace and view the instructions under the welcome message https://marketplace.zestrahub.test/welcome
2. Download Zestra Editor: https://support.zestrahub.test/entries/58104926-zestra-editor
3. Use the free templates provided in this brief to create your designs and submit to ArtFlock
Updates

Reason: Due to the Christmas break we are extending the deadline of our competition. Thank you for time and effort - I will be providing feedback over the next couple of days! Best wishes, Melody

Hi All,

I have received many screenshots with some great designs! I just wanted to clarify that you are designing Zestra app templates including Zestra features and not just page designs?

Read Tips for First Time Zestrans to guide you through the template creation process

Before you start designing templates for Zestra Marketplace

·       Read the Quality Standards

·       Read the Copyright Information 

·       Use the Template Quality Checklist to ensure your template follows our guidelines. 

What should my project file contain?

·       A folder containing your source files, e.g. LayoutCraft. This must be named Source.

·       The Zestra content files. This must be named Bundle.

·       Instructions, explaining to a customer how to use your template.

Best wishes,

Melody

Reason: We are extending the competition by 7 days to give you more time!

Reason: We have received 3 complete designs for this contest so we are extending the deadline for 7 days Best wishes, Melody

Target Market(s)

Entrepreneurs who wish to create uSlate Apps by using our App design templates.

Industry/Entity Type

Fashion

Requirements
Must have
• You will need Zestra Editor to open the .oproject files attached to this brief. Get it here: https://support.zestrahub.test/entries/58104926-zestra-editor
Should not have
• • Low quality, fuzzy or blurry images
• Any stock images or content which you do not own the rights to
• Any material which could be considered inappropriate or offensive

```html
<!DOCTYPE html>
<html lang="en">
<head>
<meta charset="utf-8">
<title>Fashion – Magazine Template</title>
<link rel="stylesheet" href="https://fonts.googleapis.com/css2?family=Bowlby+One&family=Play:wght@700&family=Ubuntu:wght@400;500;700&display=swap">
<style>
  :root {
    --bar-black: #000000;
    --header-top: #27a9e1;
    --header-bottom: #0a78b6;
    --header-text: #0e5a7c;
    --headline-blue: #0aa2ea;
    --panel-black: #000000;
    --list-bg: #f1f2f3;
    --title-blue: #1b93c8;
    --body-grey: #5d5f61;
    --frame-white: #ffffff;
    --button-top: #5cc6f2;
    --button-bottom: #1786c4;
    --button-text: #0b4c74;
    --footer-top: #f7f8f9;
    --footer-bottom: #c9cccf;
    --nav-blue: #0b7fbf;
  }
  * { box-sizing: border-box; margin: 0; padding: 0; }
  html, body { width: 948px; height: 1200px; overflow: hidden; background: var(--list-bg); }
  .screen { width: 948px; height: 1200px; display: flex; flex-direction: column; }

  .status-bar {
    height: 33px; background: var(--bar-black); color: #fff;
    display: flex; align-items: center; justify-content: space-between;
    padding: 0 6px 0 6px; font: 700 18px/1 "Ubuntu", sans-serif; position: relative;
  }
  .status-left { display: flex; align-items: center; gap: 10px; }
  .status-time { position: absolute; left: 50%; transform: translateX(-50%); }
  .status-right { display: flex; align-items: center; gap: 12px; }

  .section-header {
    height: 96px;
    background: linear-gradient(var(--header-top), var(--header-bottom));
    border-bottom: 3px solid #7fd0f2;
    display: flex; align-items: center; justify-content: center;
  }
  .section-title {
    font: 700 54px/1 "Play", sans-serif; color: var(--header-text);
    letter-spacing: 1px; text-shadow: 0 1px 0 rgba(255,255,255,.25);
  }

  .hero { height: 555px; display: flex; }
  .hero-photo {
    width: 580px; height: 100%;
    background:
      radial-gradient(ellipse 30% 45% at 50% 50%, #d8292c 0%, #c8272b 45%, transparent 70%),
      radial-gradient(ellipse 40% 40% at 45% 85%, #f08a2c 0%, transparent 70%),
      linear-gradient(90deg, #7a2a12 0%, #b4491c 20%, #3d5f78 50%, #b4491c 80%, #6e2510 100%);
  }
  .hero-panel {
    flex: 1; background: var(--panel-black);
    padding: 34px 0 0 24px;
  }
  .hero-headline {
    font: 400 54px/70px "Bowlby One", sans-serif; color: var(--headline-blue);
    text-transform: uppercase; letter-spacing: -1px;
  }

  .article-list {
    height: 443px; background: var(--list-bg);
    padding: 29px 34px 0 27px;
    display: flex; flex-direction: column; gap: 36px;
  }
  .article { display: flex; gap: 25px; }
  .article-thumb {
    width: 275px; height: 173px; flex: none;
    background: var(--frame-white); padding: 5px;
    box-shadow: 0 1px 4px rgba(0,0,0,.35);
  }
  .thumb-fill { width: 100%; height: 100%; }
  .thumb-portrait { background: radial-gradient(ellipse 40% 60% at 55% 55%, #e8c98a 0%, #b99657 45%, #111 80%); }
  .thumb-runway { background: radial-gradient(ellipse 30% 55% at 45% 60%, #d2222a 0%, #a8323a 45%, transparent 70%), linear-gradient(#6d6a78, #8c8a93 60%, #4d6a3e); }
  .article-body { padding-top: 2px; }
  .article-title {
    font: 500 26px/1 "Ubuntu", sans-serif; color: var(--title-blue);
    margin-bottom: 12px;
  }
  .article-text {
    font: 400 14.5px/20px "Ubuntu", sans-serif; color: var(--body-grey);
    width: 540px;
  }
  .more-button {
    display: inline-block; margin-top: 18px;
    width: 60px; height: 31px; padding-left: 9px;
    font: 700 14.5px/31px "Ubuntu", sans-serif; color: var(--button-text);
    background: linear-gradient(var(--button-top), var(--button-bottom));
    clip-path: polygon(0 0, 78% 0, 100% 50%, 78% 100%, 0 100%);
    border-radius: 4px 0 0 4px;
  }

  .footer-bar {
    height: 73px;
    background: linear-gradient(var(--footer-top), var(--footer-bottom));
    border-top: 1px solid #c4c7ca;
    display: flex; align-items: center; justify-content: flex-end;
    padding-right: 31px;
  }
  .next-button {
    width: 36px; height: 36px; background: var(--nav-blue);
    border-radius: 2px; display: flex; align-items: center; justify-content: center;
  }
</style>
</head>
<body>
<main class="screen">
  <div class="status-bar">
    <div class="status-left">
      <span class="device-name">uSlate</span>
      <svg width="22" height="16" viewBox="0 0 22 16" aria-hidden="true">
        <path d="M1 6a14 14 0 0 1 20 0" stroke="#fff" stroke-width="2.4" fill="none"/>
        <path d="M4.5 9.5a9 9 0 0 1 13 0" stroke="#fff" stroke-width="2.4" fill="none"/>
        <path d="M8 13a4 4 0 0 1 6 0" stroke="#fff" stroke-width="2.4" fill="none"/>
      </svg>
    </div>
    <span class="status-time">4:20 PM</span>
    <div class="status-right">
      <svg width="16" height="16" viewBox="0 0 16 16" aria-hidden="true">
        <circle cx="8" cy="8" r="7" fill="#fff"/>
        <path d="M8 3.5V8H5" stroke="#000" stroke-width="1.8" fill="none"/>
      </svg>
      <svg width="32" height="16" viewBox="0 0 32 16" aria-hidden="true">
        <rect x="1" y="1" width="27" height="14" rx="2" stroke="#fff" stroke-width="1.6" fill="none"/>
        <rect x="3.5" y="3.5" width="22" height="9" fill="#fff"/>
        <rect x="28.5" y="5" width="2.5" height="6" fill="#fff"/>
      </svg>
    </div>
  </div>

  <header class="section-header">
    <h1 class="section-title">FASHION</h1>
  </header>

  <section class="hero">
    <div class="hero-photo" role="img" aria-label="Runway model in a red, blue and orange feathered festive costume"></div>
    <div class="hero-panel">
      <h2 class="hero-headline">This<br>week<br>top<br>walk<br>in<br>festive<br>mood</h2>
    </div>
  </section>

  <section class="article-list">
    <article class="article">
      <div class="article-thumb"><div class="thumb-fill thumb-portrait" role="img" aria-label="Portrait of a blonde model with bold blue eye make-up"></div></div>
      <div class="article-body">
        <h3 class="article-title">LOREL IPSUM DOLOR SIT AMET</h3>
        <p class="article-text">Lorem ipsum dolor sit amet, consectetur adipiscing elit. Fusce lacus magna, pulvinar in consequat vitae, tristique sed nulla. Maecenas tempor velit dui. Nam elit erat, semper iaculis condimentum vitae, accumsan sit amet arcu. Cras consectetur arcu vel sem dictum hendrerit faucibus risus lacinia.</p>
        <a class="more-button" href="#">More</a>
      </div>
    </article>
    <article class="article">
      <div class="article-thumb"><div class="thumb-fill thumb-runway" role="img" aria-label="Model in a red dress on the runway holding clear balloons"></div></div>
      <div class="article-body">
        <h3 class="article-title">LOREL IPSUM DOLOR SIT AMET</h3>
        <p class="article-text">Lorem ipsum dolor sit amet, consectetur adipiscing elit. Fusce lacus magna, pulvinar in consequat vitae, tristique sed nulla. Maecenas tempor velit dui. Nam elit erat, semper iaculis condimentum vitae, accumsan sit amet arcu. Cras consectetur arcu vel sem dictum hendrerit faucibus risus lacinia.</p>
        <a class="more-button" href="#">More</a>
      </div>
    </article>
  </section>

  <footer class="footer-bar">
    <a class="next-button" href="#" aria-label="Next page">
      <svg width="16" height="22" viewBox="0 0 16 22" aria-hidden="true">
        <path d="M4 3l8 8-8 8" stroke="#fff" stroke-width="3" fill="none"/>
      </svg>
    </a>
  </footer>
</main>
</body>
</html>
```